DOUBLE SIDED BROCHURE NEEDED TO PROMOTE DOCTOR

I need a double sided DL size (99mm x 210mm) brochure, promoting a doctor seeing patients in a new area.

I want something professional. I have included the relevant information. I would also like the Dr's picture somwhere in the brochure, with a professional background. I wish to print these tomorrow, so i will pick a winner within 14 hours of posting this ad.

I have included an example of a brochures design that I recently saw, and its definietly a good starting point.

Medical

```html
<!DOCTYPE html>
<html lang="en">
<head>
<meta charset="utf-8">
<title>Dr. Omar Haddad – Seabrook Consulting DL Brochure</title>
<link rel="stylesheet" href="https://fonts.googleapis.com/css2?family=Jost:wght@400;500&family=Montserrat:wght@700&family=Arimo:wght@400;700&display=swap">
<style>
  :root {
    --blue: #3d82c6;
    --yellow: #e0dd1f;
    --white: #ffffff;
    --stage: #e6e9eb;
    --photo-sky: #bcd3ea;
    --photo-mid: #8a8f99;
    --photo-dark: #2f3440;
  }
  * { box-sizing: border-box; margin: 0; padding: 0; }
  html, body { width: 1143px; height: 1200px; overflow: hidden; }
  body { background: var(--stage); position: relative; }

  .panel {
    position: absolute;
    top: 89px;
    width: 482px;
    height: 1022px;
    background: var(--blue);
    overflow: hidden;
    box-shadow: 0 4px 14px rgba(0,0,0,.25);
  }
  .panel--front { left: 94px; }
  .panel--back { left: 601px; }

  /* Front panel */
  .hero { position: absolute; left: 0; top: 0; width: 482px; height: 440px; }
  .letter {
    position: absolute; left: 38px; top: 434px; width: 430px;
    font-family: "Jost", sans-serif; color: var(--white);
    font-size: 24px; line-height: 33px; letter-spacing: .3px;
    white-space: nowrap;
  }
  .announce {
    font-family: "Montserrat", sans-serif; font-weight: 700;
    color: var(--yellow); font-size: 33px; line-height: 42px;
    letter-spacing: 1px; margin: 2px 0 0;
  }
  .clinic {
    position: absolute; right: 30px; top: 842px; text-align: right;
    font-family: "Jost", sans-serif; font-style: normal; color: var(--yellow);
    font-size: 21.5px; line-height: 29px; letter-spacing: .6px;
  }
  .referrals {
    position: absolute; right: 40px; top: 951px;
    font-family: "Jost", sans-serif; color: var(--white); font-size: 14px;
  }
  .rule { position: absolute; left: 0; right: 0; top: 977px; height: 9px; background: var(--yellow); }
  .corner { position: absolute; border-radius: 50%; background: var(--yellow); }
  .corner--front { left: -70px; top: 935px; width: 174px; height: 174px; }

  /* Back panel */
  .corner--top { right: -92px; top: -104px; width: 190px; height: 190px; }
  .corner--bottom { right: -92px; bottom: -92px; width: 192px; height: 192px; }
  .claim {
    position: absolute; left: 54px; top: 56px; width: 420px;
    font-family: "Arimo", sans-serif; font-weight: 700;
    color: var(--white); font-size: 38.5px; line-height: 51.5px; letter-spacing: -.6px;
    white-space: nowrap;
  }
  .claim em { font-style: normal; color: var(--yellow); }
  .services {
    position: absolute; left: 0; top: 391px; width: 375px; height: 527px;
    background: var(--yellow);
    box-shadow: 6px 8px 14px rgba(0,0,0,.35);
    font-family: "Arimo", sans-serif; color: var(--blue);
  }
  .services h2 { position: absolute; left: 59px; top: 30px; font-weight: 400; font-size: 27px; }
  .services ul { position: absolute; left: 0; top: 66px; list-style: none; }
  .services li { position: relative; padding-left: 61px; font-size: 21.5px; line-height: 33px; white-space: nowrap; }
  .services li.tick::before {
    content: ""; position: absolute; left: 24px; top: 9px; width: 22px; height: 20px;
    background: var(--white);
    clip-path: polygon(0 55%, 18% 42%, 38% 70%, 86% 0, 100% 12%, 40% 100%);
  }
</style>
</head>
<body>
  <section class="panel panel--front">
    <svg class="hero" viewBox="0 0 482 440" role="img" aria-label="Photo of the doctor in front of a modern hospital building">
      <defs>
        <linearGradient id="heroTone" x1="0" y1="0" x2="1" y2="1">
          <stop offset="0" stop-color="var(--photo-sky)"/>
          <stop offset=".55" stop-color="var(--photo-mid)"/>
          <stop offset="1" stop-color="var(--photo-dark)"/>
        </linearGradient>
      </defs>
      <rect width="482" height="440" fill="url(#heroTone)"/>
      <path d="M0 350 C90 400 200 430 300 420 C380 412 440 400 482 385 L482 440 L0 440 Z" fill="var(--yellow)"/>
      <path d="M0 362 C90 410 200 432 300 424 C380 418 440 404 482 392 L482 440 L0 440 Z" fill="var(--blue)"/>
    </svg>

    <div class="letter">
      <p>Dear Doctors,<br>We are pleased to announce that</p>
      <h1 class="announce">DR. OMAR HADDAD<br>IS NOW CONSULTING<br>IN SEABROOK,</h1>
      <p>seeing public and private patients.<br>Guaranteed appointment within two<br>weeks, with patients having the option<br>of surgery at Estuary Health Campus,<br>Wattle Grove Hospital or St. Brigid's<br>Lakeside.</p>
    </div>

    <address class="clinic">
      Seabrook Clinic: 42 Harbour View Road<br>Seabrook WA 6999.<br>1300 555 010
    </address>

    <div class="corner corner--front"></div>
    <p class="referrals">Please send all referrals by fax to (08) 5550 1234</p>
    <div class="rule"></div>
  </section>

  <section class="panel panel--back">
    <div class="corner corner--top"></div>
    <div class="corner corner--bottom"></div>

    <h2 class="claim">Dr. Haddad is a<br><em>HIGHLY TRAINED<br>SPECIALISED</em><br>surgeon, in all areas<br>of <em>Endocrine, Breast<br>and General Surgery.</em></h2>

    <div class="services">
      <h2>Including :</h2>
      <ul>
        <li class="tick">Thyroid Surgery</li>
        <li>Parathyroid surgery (including</li>
        <li>minimally invasive</li>
        <li class="tick">parathyroidectomy)</li>
        <li class="tick">Breast Cancer</li>
        <li class="tick">Benign breast lesions</li>
        <li>All areas of general surgery,</li>
        <li>such as;</li>
        <li class="tick">Gallbladder surgery</li>
        <li class="tick">Hernia surgery</li>
        <li class="tick">Haemorrhoids</li>
        <li class="tick">Carpal Tunnel</li>
        <li class="tick">Vasectomy…</li>
      </ul>
    </div>
  </section>
</body>
</html>
```